Business Card Design Project

Need a business card which is crisp, clear and modern.
with the logo being highlighted and at the back of the card our services.
Please use the attached logo for creating the cards.

Reason: need to receive some good designs

Target Market(s)

Our target customers will be hotels, offices, single users

Industry/Entity Type

Business

```html
<!DOCTYPE html>
<html lang="en">
<head>
<meta charset="utf-8">
<title>Parlunet Business Card</title>
<link rel="stylesheet" href="https://fonts.googleapis.com/css2?family=Open+Sans:wght@400;600&display=swap">
<style>
  :root {
    --canvas-bg: #ecebea;
    --card-bg: #ffffff;
    --ink: #2b2b2b;
    --muted: #8a8a8a;
    --accent: #e4177f;
  }
  * { box-sizing: border-box; margin: 0; padding: 0; }
  html, body { width: 1200px; height: 869px; overflow: hidden; }
  body {
    background: var(--canvas-bg);
    font-family: "Open Sans", sans-serif;
    position: relative;
  }
  .card {
    position: absolute;
    width: 520px;
    height: 300px;
    background: var(--card-bg);
    border-radius: 16px;
    box-shadow: 0 6px 18px rgba(0,0,0,0.18);
    overflow: hidden;
  }
  .card--back { left: 50px; top: 150px; }
  .card--front { left: 630px; top: 420px; }

  .back-brand {
    position: absolute;
    inset: 0;
    display: flex; align-items: center; justify-content: center; gap: 18px;
  }
  .back-brand__dot {
    width: 64px; height: 64px; border-radius: 50%;
    background: var(--accent);
  }
  .back-brand__name {
    font-size: 58px; font-weight: 600; color: var(--ink);
  }

  .brand {
    position: absolute; left: 36px; top: 44px;
    display: flex; align-items: center; gap: 12px;
  }
  .brand__dot {
    width: 40px; height: 40px; border-radius: 50%;
    background: var(--accent);
  }
  .brand__name {
    font-size: 30px; font-weight: 600; color: var(--ink);
  }

  .details {
    position: absolute; right: 56px; bottom: 22px;
    text-align: right;
  }
  .details__name { font-size: 30px; font-weight: 400; color: var(--ink); line-height: 1.1; }
  .details__role { font-size: 20px; color: var(--accent); line-height: 1.3; }
  .contact { margin-top: 22px; font-size: 16px; line-height: 1.35; color: var(--muted); }
  .contact__web { color: var(--ink); }
  .accent-rule {
    position: absolute; right: 40px; top: 128px; bottom: 16px;
    width: 3px; background: var(--accent);
  }
</style>
</head>
<body>
  <section class="card card--back" aria-label="Card back">
    <div class="back-brand">
      <span class="back-brand__dot"></span>
      <span class="back-brand__name">Parlunet</span>
    </div>
  </section>

  <section class="card card--front" aria-label="Card front">
    <div class="brand">
      <span class="brand__dot"></span>
      <span class="brand__name">Parlunet</span>
    </div>
    <div class="details">
      <p class="details__name">Maya Collins</p>
      <p class="details__role">manager</p>
      <div class="contact">
        <p>000 000 0000 000</p>
        <p>maya.c@parlunet.com</p>
        <p class="contact__web">www.parlunet.com</p>
      </div>
    </div>
    <span class="accent-rule"></span>
  </section>
</body>
</html>
```